ROVN branded stationary template

We need associated stationary to accompany our new logo.

The stationary design will be used on business cards, presentation slides and document templates so needs to be provided in an EPS format so that we can adapt it. The design MUST BE ADAPTABLE.

The logo colour is #4a4195 or RGB 85/68/141. Associated colours that can be used in this stationary should compliment this colour. Other colour choices - the preference would be dark and light purples, blues, black and greys. Done how you see fit.

We want the stationary to compliment the overall design of the logo, so clean sharp lines are what we are looking for. It doesn't need to be overly intricate in design - something simple that compliments the look and feel of the logo is what we want. More focused on lines and shapes around the stationary, not any additional logos or pictures.

UK housing providers

Business

Sans Serif

• Clean sharp appearance, nothing overly elaborate.

```html
<!DOCTYPE html>
<html lang="en">
<head>
<meta charset="utf-8">
<title>ROVN business card</title>
<link rel="stylesheet" href="https://fonts.googleapis.com/css2?family=Open+Sans:wght@400;600;700&display=swap">
<style>
  :root {
    --backdrop: #3b3b3d;
    --card-white: #ffffff;
    --brand-purple: #655fa9;
    --band-grey: #5a5a5b;
    --text-grey: #4a4a4a;
    --icon-purple: #5f58a3;
  }
  * { margin: 0; padding: 0; box-sizing: border-box; }
  html, body {
    width: 1105px;
    height: 1200px;
    overflow: hidden;
    background: var(--backdrop);
    font-family: "Open Sans", Arial, sans-serif;
  }
  .canvas { position: relative; width: 1105px; height: 1200px; }

  .card {
    position: absolute;
    left: 196px;
    width: 720px;
    height: 412px;
    overflow: hidden;
  }
  .card--front { top: 146px; background: var(--card-white); }
  .card--back { top: 602px; background: var(--brand-purple); }

  /* front: name band */
  .name-band { position: absolute; left: 0; top: 58px; }
  .holder { position: absolute; left: 40px; top: 64px; color: #fff; }
  .holder__name { font-size: 25px; font-weight: 600; line-height: 1.1; }
  .holder__role { font-size: 19px; font-weight: 400; line-height: 1.3; }

  /* wordmark */
  .wordmark {
    position: absolute;
    display: flex;
    align-items: center;
    font-weight: 700;
    letter-spacing: 1px;
  }
  .wordmark__square { display: block; background: currentColor; }
  .card--front .wordmark {
    right: 48px; top: 62px;
    color: var(--brand-purple);
    font-size: 54px; gap: 18px; line-height: 1;
  }
  .card--front .wordmark__square { width: 40px; height: 40px; }
  .card--back .wordmark {
    left: 50%; top: 50%;
    transform: translate(-50%, -50%);
    color: #fff;
    font-size: 86px; gap: 30px; line-height: 1;
  }
  .card--back .wordmark__square { width: 66px; height: 66px; }

  /* contacts */
  .contacts { position: absolute; left: 34px; top: 245px; list-style: none; }
  .contacts__item {
    display: flex; align-items: center; gap: 10px;
    height: 27.5px;
    font-size: 19px; color: var(--text-grey);
  }
  .contacts__icon { width: 18px; height: 18px; fill: var(--icon-purple); flex: none; }

  .address {
    position: absolute; right: 38px; top: 266px;
    text-align: right; font-style: normal;
    font-size: 19px; line-height: 27px; color: var(--text-grey);
  }
  .address__web { letter-spacing: 2px; }
  .address__web strong { color: var(--brand-purple); font-weight: 700; }

  .foot-band { position: absolute; left: 0; bottom: 0; }
</style>
</head>
<body>
<main class="canvas">

  <section class="card card--front" aria-label="Business card front">
    <svg class="name-band" width="720" height="72" viewBox="0 0 720 72" aria-hidden="true">
      <polygon points="0,0 421,0 421,68 0,68" fill="var(--band-grey)"/>
      <rect x="0" y="68" width="490" height="3" fill="var(--band-grey)"/>
    </svg>
    <div class="holder">
      <p class="holder__name">Daniel Hart</p>
      <p class="holder__role">CEO/Founder</p>
    </div>

    <div class="wordmark"><span class="wordmark__square"></span><span>ROVN</span></div>

    <ul class="contacts">
      <li class="contacts__item">
        <svg class="contacts__icon" viewBox="0 0 24 24" aria-hidden="true"><path d="M6.6 10.8a15.1 15.1 0 0 0 6.6 6.6l2.2-2.2a1 1 0 0 1 1-.25 11.4 11.4 0 0 0 3.6.57 1 1 0 0 1 1 1V20a1 1 0 0 1-1 1A17 17 0 0 1 3 4a1 1 0 0 1 1-1h3.5a1 1 0 0 1 1 1c0 1.25.2 2.45.57 3.57a1 1 0 0 1-.25 1z"/></svg>
        614 275 8093
      </li>
      <li class="contacts__item">
        <svg class="contacts__icon" viewBox="0 0 24 24" aria-hidden="true"><path d="M7 1h10a2 2 0 0 1 2 2v18a2 2 0 0 1-2 2H7a2 2 0 0 1-2-2V3a2 2 0 0 1 2-2zm0 3v14h10V4zm5 15.5a1.2 1.2 0 1 0 0 2.4 1.2 1.2 0 0 0 0-2.4z"/></svg>
        752 319 6480
      </li>
      <li class="contacts__item">
        <svg class="contacts__icon" viewBox="0 0 24 24" aria-hidden="true"><path d="M6 2h9l3 3v4H6zM3 10h18a1 1 0 0 1 1 1v7h-4v4H6v-4H2v-7a1 1 0 0 1 1-1zm5 6v4h8v-4z"/></svg>
        397 508 2146
      </li>
      <li class="contacts__item">
        <svg class="contacts__icon" viewBox="0 0 24 24" aria-hidden="true"><path d="M2 5h20v14H2zm2 2v.5l8 5 8-5V7z"/></svg>
        hello@rovnhomes.com
      </li>
    </ul>

    <address class="address">
      2148 Alder Crescent<br>
      Fairbury, Ohio 45812<br>
      <span class="address__web">www.<strong>rovnhomes</strong>.com</span>
    </address>

    <svg class="foot-band" width="720" height="21" viewBox="0 0 720 21" aria-hidden="true">
      <polygon points="0,0 464,0 460,21 0,21" fill="var(--brand-purple)"/>
      <polygon points="471,0 720,0 720,21 467,21" fill="var(--band-grey)"/>
    </svg>
  </section>

  <section class="card card--back" aria-label="Business card back">
    <div class="wordmark"><span class="wordmark__square"></span><span>ROVN</span></div>
  </section>

</main>
</body>
</html>
```